LumaVantix
stationery - business cards
LumaVantix -
Creative Brief
Professional
Carl MORVEDO
41 Pellin Lane, suite 218 San Mateo, California, 94402
cm@lumavantix.com
www.lumavantix.com
Free to be creative

```html
<!DOCTYPE html>
<html lang="en">
<head>
<meta charset="utf-8">
<title>LumaVantix Stationery</title>
<link href="https://fonts.googleapis.com/css2?family=Tinos:wght@400;700&display=swap" rel="stylesheet">
<style>
  :root {
    --board: #2a2a2a;
    --board-edge: #3a3a3a;
    --paper: #f4f4f5;
    --paper-shade: #dedfe1;
    --brand-blue: #1565c0;
    --brand-blue-light: #3d8be0;
    --brand-blue-dark: #0b3f86;
    --logo-grey: #6d6e71;
    --text-dark: #333336;
    --link-blue: #1f6fc6;
  }
  * { box-sizing: border-box; margin: 0; padding: 0; }
  html, body { width: 1200px; height: 871px; overflow: hidden; background: #8a8a8a; }
  body { font-family: "Tinos", "Times New Roman", serif; color: var(--text-dark); }

  .board {
    position: relative; width: 1200px; height: 871px;
    background: var(--board); border: 2px solid var(--board-edge); border-radius: 14px;
  }
  .sheet { position: absolute; box-shadow: 0 4px 14px rgba(0,0,0,.55); overflow: hidden; }
  .soft-squares {
    position: absolute; inset: 0;
    background:
      radial-gradient(ellipse at 70% 35%, #ffffff 0%, rgba(255,255,255,0) 45%),
      radial-gradient(ellipse at 35% 70%, #ffffff 0%, rgba(255,255,255,0) 40%),
      linear-gradient(160deg, var(--paper) 0%, var(--paper-shade) 100%);
  }

  .logo { position: absolute; display: flex; align-items: center; gap: 8px; color: var(--logo-grey); }
  .logo-square { background: var(--logo-grey); flex: none; }
  .logo-name { font-weight: 400; white-space: nowrap; line-height: 1; }
  .logo--light { color: #ffffff; }
  .logo--light .logo-square { background: #ffffff; }

  .contact { position: absolute; font-size: 11px; line-height: 1.35; font-style: normal; white-space: nowrap; }
  .contact .email { color: var(--link-blue); }
  .accent-bar { position: absolute; background: var(--brand-blue); }

  /* letterhead */
  .letterhead { left: 36px; top: 12px; width: 444px; height: 833px; }
  .letterhead .logo { left: 12px; top: 20px; }
  .letterhead .logo-square { width: 40px; height: 40px; }
  .letterhead .logo-name { font-size: 34px; }
  .letterhead .accent-bar { left: 0; top: 770px; width: 8px; height: 52px; }
  .letterhead .contact { left: 14px; top: 770px; font-size: 10px; }

  /* envelope */
  .envelope { left: 228px; top: 408px; width: 768px; height: 437px; }
  .envelope-flap {
    position: absolute; left: 0; top: 0; width: 100%; height: 72px;
    background: linear-gradient(180deg, var(--brand-blue-light), var(--brand-blue));
  }
  .flap-mark { position: absolute; left: 370px; top: 16px; width: 30px; height: 30px; background: #fff; }
  .envelope .logo { left: 14px; top: 100px; }
  .envelope .logo-square { width: 34px; height: 34px; }
  .envelope .logo-name { font-size: 30px; }
  .envelope .accent-bar { left: 0; top: 300px; width: 9px; height: 42px; }
  .envelope .contact { left: 16px; top: 308px; }

  /* business cards */
  .card { top: 233px; height: 151px; border-radius: 10px; }
  .card-front {
    left: 648px; width: 259px;
    background: linear-gradient(150deg, var(--brand-blue-light) 0%, var(--brand-blue) 50%, var(--brand-blue-dark) 100%);
  }
  .card-front .logo { left: 50%; top: 50px; transform: translateX(-50%); }
  .card-front .logo-square { width: 26px; height: 26px; }
  .card-front .logo-name { font-size: 24px; }
  .card-front .website {
    position: absolute; left: 0; right: 0; bottom: 12px; text-align: center;
    color: #dfe9f7; font-size: 9px; letter-spacing: .5px;
  }
  .card-back { left: 919px; width: 262px; }
  .card-back .logo { right: 14px; top: 12px; }
  .card-back .logo-square { width: 18px; height: 18px; }
  .card-back .logo-name { font-size: 18px; }
  .card-back .contact { left: 16px; top: 62px; font-size: 8.5px; }
  .card-back .holder-name {
    position: absolute; right: 18px; top: 122px; font-size: 11px; color: var(--text-dark);
  }
</style>
</head>
<body>
<main class="board">

  <section class="sheet letterhead">
    <div class="soft-squares" role="img" aria-label="Soft white rounded-square background pattern"></div>
    <div class="logo"><span class="logo-square"></span><span class="logo-name">LumaVantix</span></div>
    <span class="accent-bar"></span>
    <address class="contact">
      41 Pellin Lane, suite 218<br>
      Alder Springs, Oregon, 97321<br>
      P: (800) 417 2290<br>
      <span class="email">E: cm@lumavantix.com</span>
    </address>
  </section>

  <section class="sheet envelope">
    <div class="soft-squares" role="img" aria-label="Soft white rounded-square background pattern"></div>
    <div class="envelope-flap"><span class="flap-mark"></span></div>
    <div class="logo"><span class="logo-square"></span><span class="logo-name">LumaVantix</span></div>
    <span class="accent-bar"></span>
    <address class="contact">
      41 Pellin Lane, suite 218<br>
      Alder Springs, Oregon, 97321
    </address>
  </section>

  <section class="sheet card card-front">
    <div class="logo logo--light"><span class="logo-square"></span><span class="logo-name">LumaVantix</span></div>
    <p class="website">www.lumavantix.com</p>
  </section>

  <section class="sheet card card-back">
    <div class="soft-squares" role="img" aria-label="Soft white rounded-square background pattern"></div>
    <div class="logo"><span class="logo-square"></span><span class="logo-name">LumaVantix</span></div>
    <address class="contact">
      41 Pellin Lane, suite 218<br>
      Alder Springs, Oregon, 97321<br>
      P: (800) 417 2290<br>
      <span class="email">E: cm@lumavantix.com</span>
    </address>
    <p class="holder-name">CARL MORVEDO</p>
  </section>

</main>
</body>
</html>
```